KETRAV Website - Innovative Products need a creative designer!

I require a bold, fun and interactive website designing for my company rebrand. I am in the process of having new logo's designed but the colour scheme is already established.

Colours: Yellow (PRIMARY) : #C6FF02 / RGB: 198, 255, 2 Black (SECONDARY): #000000 / RGB: 0, 0, 0

The company specialises in Temporary Modular Space, so i would like to see creative blocks illustrating the products. (Products listed below). Please only design the homepage and the winner will then design / code the full thing. Please include an area that elaborates on the sustainablity factor of the company. I like animated emblems, pictures and writing. There will be on going work on this, as I will need the designer to provide up keep and maintenance on it as we progress.

Menu Pages:

The Solutions - (Products):
Wandlock: An innovative point of sale units specifically designed for the sale of Merchandise. It transports like a normal shipping container, but once situated expands outwards to increase the internal footprint by up to 90%. And once in situ are completely antivandal, removing the requirement for multiple security personnel and protecting your products. It also provide sales points to a 180 degree angle, maximising revenue and reducing queue time. - Completely customisable.

Roostel: A penthouse in a box, the innovative nature of the unit enables it to be situated anywhere. Ideal for glamping sites, guest houses at private properties for temporary Festival accommodation. The unit comes fully furnished with a kitchenette, en suite bathroom and ample space for a double bed and a living area. This is truly the luxurious and affordable option for temporary accommodation.

Glimcase: A standalone product, but also an accessory to the Wandlock. A flat pack system that is truly 100% modular, all wall panels can be installed tailored to your requirements. This can be an on site office, or a glass display box for brand activations. Installed on the ground or on the roof of the Wandlock, it is a flexible piece of equipment designed that is not only premium but affordable. - Completely customisable.

PLRange:
PL10: A quick install and sustainable design for use on a variety of sites. The cabins collapse down enabling multiple units to be transported on a 1no. truck. We can transport 20no. units on 1no. 40ft truck, reducing the carbon footprint of events drastically. When erected, they can be stacked to create 2no. floors. - Completely customisable.
PL20: Same as the above but a 20ft cabin. These can transport 10no. units on a 40ft trailer. Can be stacked to create 2no. floors. - Completely customisable.

The Industries:
Merchandise & Shows
Sports & Stadia
Brand Activations
Retail & Stores
Events & Festivals
Automotive
Exhibitions

The Company: Will confirm all information once the winner is selected.

Contact: Will confirm all information once the winner is selected.

Events, Merchandise, Stadiums, Automotive, Brand Activations, Commercial

Must have
• Interactive elements, engaging design, innovative movements, be bright and bold. But most importantly be informative and easy to navigate.
Nice to have
• Animations of blocks, moving emblems.
Should not have
• No pre existing templates

```html
<!DOCTYPE html>
<html lang="en">
<head>
<meta charset="utf-8">
<title>KETRAV – Temporary Modular Space</title>
<link rel="stylesheet" href="https://fonts.googleapis.com/css2?family=Exo+2:wght@600;700;800&family=Roboto:wght@400;500;700&display=swap">
<style>
:root{
  --lime:#c6ff02;
  --black:#000;
  --white:#fff;
  --panel:#2a2a2a;
  --hex:#2b2b2b;
  --muted:#6f8a10;
  --head:"Exo 2",sans-serif;
  --body:"Roboto",Arial,sans-serif;
}
*{box-sizing:border-box;margin:0;padding:0}
html,body{width:1200px;height:5148px;overflow:hidden;background:var(--black);font-family:var(--body);color:var(--white)}
section,header,footer,nav{position:relative;width:1200px;overflow:hidden}
.abs{position:absolute}
.hexclip{clip-path:polygon(50% 0,100% 25%,100% 75%,50% 100%,0 75%,0 25%)}

/* top bar */
.topbar{height:36px;background:var(--black);font-size:12px}
.topbar .item{position:absolute;top:11px;display:flex;align-items:center;gap:6px}
.topbar svg{width:11px;height:11px;fill:var(--lime)}
.socials{position:absolute;top:7px;left:928px;display:flex;gap:10px}
.socials span{width:22px;height:22px;border-radius:50%;background:#3a3a3a;display:block}

/* nav */
.mainnav{height:82px;background:var(--lime);color:var(--black)}
.brand{position:absolute;left:145px;top:24px;display:flex;align-items:center;gap:10px;font-family:var(--head);font-weight:800;font-size:30px;letter-spacing:1px;color:var(--black)}
.brand .mark{width:26px;height:26px;background:var(--black)}
.menu{position:absolute;right:145px;top:32px;display:flex;gap:22px;font-size:14px;font-weight:500}

/* hero */
.hero{height:682px;background:var(--black)}
.hero-photo{position:absolute;inset:0;background:linear-gradient(100deg,#2a241d 0%,#5b4633 35%,#7a5d3d 55%,#3b332b 75%,#8d8a84 100%)}
.hero-shade{position:absolute;inset:0;background:rgba(0,0,0,.28)}
.hero h1{position:absolute;top:168px;width:100%;text-align:center;font-family:var(--head);font-weight:800;font-size:44px;letter-spacing:1px}
.hero p{position:absolute;top:232px;left:370px;width:460px;text-align:center;font-size:16px;line-height:24px;font-weight:500}
.btn-lime{background:var(--lime);color:var(--black);font-weight:700;font-size:14px;display:flex;align-items:center;justify-content:center;gap:8px;text-transform:uppercase}
.hero .btn-lime{position:absolute;left:515px;top:304px;width:170px;height:48px;font-size:15px}
.arrow{position:absolute;top:246px;width:34px;height:34px;border-radius:50%;background:rgba(0,0,0,.45);display:flex;align-items:center;justify-content:center}
.arrow svg{width:12px;height:12px;stroke:#fff;stroke-width:2.5;fill:none}
.hero-edge{position:absolute;left:0;top:422px;width:1200px;height:260px}

/* headings */
.sec-title{position:absolute;width:100%;text-align:center;font-family:var(--head);font-weight:700;font-size:38px;letter-spacing:.5px}
.sec-title em,.about h2 em{font-style:normal;color:var(--lime)}
.bar{position:absolute;height:4px;width:90px;background:var(--lime)}
.bar.center{left:555px}

/* solutions */
.solutions{height:1620px}
.product-hex{position:absolute;width:364px;height:420px}
.product-hex .ph{width:100%;height:100%;background:radial-gradient(circle at 50% 45%,#b8ec12 0%,#8fbf0a 45%,#4f6a06 100%)}
.product h3{position:absolute;font-family:var(--head);font-weight:700;font-size:32px;letter-spacing:.5px}
.product .copy{position:absolute;width:422px;font-size:13px;line-height:22px;text-align:justify}
.product .copy p+p{margin-top:12px}
.btn-white{position:absolute;width:152px;height:45px;background:var(--white);color:var(--black);font-weight:700;font-size:13px;display:flex;align-items:center;justify-content:center;gap:7px}
.btn-white svg,.btn-lime svg{width:13px;height:13px}

/* plrange */
.plrange{height:540px}
.panel{position:absolute;top:85px;width:590px;height:450px;background:var(--panel)}
.panel.left{left:0;clip-path:polygon(0 0,100% 8%,100% 92%,0 100%)}
.panel.right{left:610px;clip-path:polygon(0 8%,100% 0,100% 100%,0 92%)}
.panel .strip{position:absolute;top:95px;width:375px;height:65px;background:linear-gradient(90deg,#8d8d8d,#e9e9e9 60%,#bdbdbd)}
.panel h3{position:absolute;top:175px;font-family:var(--head);font-weight:700;font-size:20px}
.panel p{position:absolute;top:208px;width:420px;font-size:13px;line-height:24px}
.panel .btn-lime{position:absolute;top:317px;width:140px;height:40px;font-size:13px}

/* industries */
.industries{height:600px}
.ind{position:absolute;width:215px;height:250px;background:var(--hex);display:flex;flex-direction:column;align-items:center;justify-content:center;gap:14px}
.ind svg{width:64px;height:64px;fill:none;stroke:var(--lime);stroke-width:2.4;stroke-linejoin:round}
.ind span{font-size:14px;font-weight:700;text-align:center}
.ind.active{background:var(--lime);color:var(--black)}
.ind.active svg{stroke:var(--black)}

/* wave */
.wave{height:200px;background:radial-gradient(ellipse 70% 55% at 50% 55%,#4e6a06 0%,#1d2803 55%,#000 100%)}

/* about */
.about{height:530px}
.about h2{position:absolute;left:143px;top:65px;font-family:var(--head);font-weight:700;font-size:38px}
.about .copy{position:absolute;left:143px;top:160px;width:405px;font-size:13px;line-height:24px;text-align:justify}
.about .copy p+p{margin-top:10px}
.about .btn-lime{position:absolute;left:143px;top:405px;width:142px;height:45px;font-size:13px}
.about-hex{position:absolute;left:646px;top:50px;width:372px;height:430px;background:linear-gradient(150deg,#5c6b4a,#c9c9c3 45%,#8a8d90 70%,#3e4a2d)}

/* contact */
.contact{height:570px;color:var(--black)}
.contact-bg{position:absolute;inset:0}
.contact h2{position:absolute;top:135px;width:100%;text-align:center;font-family:var(--head);font-weight:700;font-size:38px}
.contact h4{position:absolute;top:205px;font-size:19px;font-weight:700}
.field{position:absolute;height:40px;background:var(--white);font-size:11px;color:#999;padding:12px 14px;display:flex;gap:6px;align-items:flex-start}
.field svg{width:10px;height:10px;stroke:#999;fill:none;stroke-width:2;margin-top:1px}
.submit{position:absolute;left:145px;top:472px;width:106px;height:38px;background:var(--black);color:var(--white);font-weight:700;font-size:13px;display:flex;align-items:center;justify-content:center}
.detail{position:absolute;left:692px;display:flex;gap:22px}
.detail svg{width:40px;height:34px;stroke:var(--black);fill:none;stroke-width:2.5;stroke-linejoin:round;stroke-linecap:round}
.detail b{display:block;font-size:14px;font-weight:700;margin-top:2px}
.detail small{display:block;font-size:13px;color:var(--muted);margin-top:8px}

/* footer */
.site-footer{height:288px;background:var(--black)}
.site-footer .brand{left:0;width:100%;justify-content:center;top:68px;color:var(--white);font-size:34px}
.site-footer .brand .mark{background:var(--white);width:30px;height:30px}
.footnav{position:absolute;top:136px;width:100%;display:flex;justify-content:center;gap:30px;font-size:12px;font-weight:700}
.footnav i{font-style:normal;font-weight:400}
.copyright{position:absolute;top:172px;width:100%;text-align:center;font-size:12px}
.copyright u{font-weight:700}
.footsocial{position:absolute;top:208px;left:508px;display:flex;gap:16px}
.footsocial span{width:40px;height:40px;border-radius:50%;background:var(--lime);display:block}
</style>
</head>
<body>

<header class="topbar">
  <div class="item" style="left:145px"><svg viewBox="0 0 12 12"><rect x="0" y="2" width="12" height="8"/></svg>info@ketrav.com</div>
  <div class="item" style="left:360px"><svg viewBox="0 0 12 12"><path d="M2 0h3l1 3-2 1.5a7 7 0 0 0 3.5 3.5L9 6l3 1v3c0 1-1 2-2 2A10 10 0 0 1 0 2c0-1 1-2 2-2z"/></svg>+1 555 014 2290</div>
  <div class="item" style="left:562px"><svg viewBox="0 0 12 12"><path d="M6 0a4.5 4.5 0 0 1 4.5 4.5C10.5 8 6 12 6 12S1.5 8 1.5 4.5A4.5 4.5 0 0 1 6 0z"/></svg>48 Harbor Lane, Westbrook, Kentshire KT4 2RD</div>
  <div class="socials"><span></span><span></span><span></span><span></span></div>
</header>

<nav class="mainnav">
  <div class="brand"><span class="mark"></span>KETRAV</div>
  <div class="menu"><span>Home</span><span>The Solutions</span><span>PLRange</span><span>The Industries</span><span>The Company</span><span>Contact Us</span></div>
</nav>

<section class="hero">
  <div class="hero-photo" role="img" aria-label="Furnished modular cabin interior with kitchenette, bar stools and wicker lounge chair"></div>
  <div class="hero-shade"></div>
  <h1>KETRAV</h1>
  <p>Lorem ipsum dolor sit amet, consectetur adipiscing elit, sed do tempor incididunt labore dolore magna aliqua.</p>
  <div class="btn-lime">Get Started <svg viewBox="0 0 14 14"><circle cx="7" cy="7" r="7" fill="#000"/><path d="M5.5 4l3 3-3 3" stroke="#c6ff02" stroke-width="1.8" fill="none"/></svg></div>
  <div class="arrow" style="left:52px"><svg viewBox="0 0 12 12"><path d="M8 1 3 6l5 5"/></svg></div>
  <div class="arrow" style="right:52px"><svg viewBox="0 0 12 12"><path d="M4 1l5 5-5 5"/></svg></div>
  <svg class="hero-edge" viewBox="0 0 1200 260" preserveAspectRatio="none">
    <polygon points="0,50 600,170 1200,50 1200,260 0,260" fill="#c6ff02" opacity=".85"/>
    <polygon points="0,90 600,255 1200,90 1200,260 0,260" fill="#000"/>
  </svg>
</section>

<section class="solutions">
  <h2 class="sec-title" style="top:60px"><em>THE</em> SOLUTIONS</h2>
  <div class="bar center" style="top:108px"></div>

  <article class="product">
    <div class="product-hex" style="left:148px;top:180px"><div class="ph hexclip" role="img" aria-label="Wandlock expanding shipping-container sales unit on a lime backdrop"></div></div>
    <h3 style="left:635px;top:222px">WANDLOCK</h3>
    <div class="copy" style="left:635px;top:280px">
      <p>An innovative point of sale units specifically designed for the sale of Merchandise. It transports like a normal shipping container, but once situated expands outwards to increase the internal footprint by up to 90%. And once in situ are completely antivandal, removing the requirement for multiple security personnel and protecting your products.</p>
      <p>It also provide sales points to a 180 degree angle, maximising revenue and reducing queue time. - Completely customisable.</p>
    </div>
    <div class="btn-white" style="left:636px;top:505px">LEARN MORE <svg viewBox="0 0 14 14"><circle cx="7" cy="7" r="7"/><path d="M5.5 4l3 3-3 3" stroke="#fff" stroke-width="1.8" fill="none"/></svg></div>
  </article>

  <article class="product">
    <h3 style="left:143px;top:722px">ROOSTEL</h3>
    <div class="copy" style="left:143px;top:780px">
      <p>A penthouse in a box, the innovative nature of the unit enables it to be situated anywhere. Ideal for glamping sites, guest houses at private properties for temporary Festival accommodation.</p>
      <p>The unit comes fully furnished with a kitchenette, en suite bathroom and ample space for a double bed and a living area. This is truly the luxurious and affordable option for temporary accommodation.</p>
    </div>
    <div class="btn-white" style="left:145px;top:965px">LEARN MORE <svg viewBox="0 0 14 14"><circle cx="7" cy="7" r="7"/><path d="M5.5 4l3 3-3 3" stroke="#fff" stroke-width="1.8" fill="none"/></svg></div>
    <div class="product-hex" style="left:690px;top:660px"><div class="ph hexclip" role="img" aria-label="Roostel furnished penthouse cabin with glass front on a lime backdrop"></div></div>
  </article>

  <article class="product">
    <div class="product-hex" style="left:145px;top:1140px"><div class="ph hexclip" role="img" aria-label="Glimcase glass display box showcasing a sports car on a lime backdrop"></div></div>
    <h3 style="left:635px;top:1192px">GLIMCASE</h3>
    <div class="copy" style="left:635px;top:1248px">
      <p>A standalone product, but also an accessory to the Wandlock. A flat pack system that is truly 100% modular, all wall panels can be installed tailored to your requirements. This can be an on site office, or a glass display box for brand activations.</p>
      <p>Installed on the ground or on the roof of the Wandlock, it is a flexible piece of equipment designed that is not only premium but affordable. - Completely customisable.</p>
    </div>
    <div class="btn-white" style="left:636px;top:1458px">LEARN MORE <svg viewBox="0 0 14 14"><circle cx="7" cy="7" r="7"/><path d="M5.5 4l3 3-3 3" stroke="#fff" stroke-width="1.8" fill="none"/></svg></div>
  </article>
</section>

<section class="plrange">
  <h2 class="sec-title" style="top:33px">PLRANGE</h2>
  <div class="bar center" style="top:80px"></div>
  <div class="panel left">
    <div class="strip" style="left:145px" role="img" aria-label="PL10 cabin unfolding sequence"></div>
    <h3 style="left:143px">PL10</h3>
    <p style="left:143px">A quick install and sustainable design for use on a variety of sites. The cabins collapse down enabling multiple units to be transported on a 1no. truck. We can transport 20no. units on 1no.</p>
    <div class="btn-lime" style="left:143px">Learn More</div>
  </div>
  <div class="panel right">
    <div class="strip" style="left:36px" role="img" aria-label="PL20 cabin unfolding sequence"></div>
    <h3 style="left:36px">PL20</h3>
    <p style="left:36px">Same as the above but a 20ft cabin. These can transport 10no. units on a 40ft trailer. Can be stacked to create 2no. floors. - Completely customisable.</p>
    <div class="btn-lime" style="left:36px">Learn More</div>
  </div>
</section>

<section class="industries">
  <h2 class="sec-title" style="top:33px"><em>THE</em> INDUSTRIES</h2>
  <div class="bar center" style="top:80px"></div>

  <div class="ind hexclip" style="left:143px;top:140px">
    <svg viewBox="0 0 64 64"><rect x="14" y="8" width="36" height="26" rx="2"/><path d="M28 15l9 6-9 6z"/><path d="M10 56v-8a6 6 0 0 1 12 0v8M26 56v-8a6 6 0 0 1 12 0v8M42 56v-8a6 6 0 0 1 12 0v8M8 56h48"/></svg>
    <span>Merchandise &amp; Shows</span></div>
  <div class="ind hexclip" style="left:375px;top:140px">
    <svg viewBox="0 0 64 64"><ellipse cx="32" cy="30" rx="26" ry="10"/><ellipse cx="32" cy="30" rx="12" ry="4"/><path d="M6 30v14c0 6 12 10 26 10s26-4 26-10V30M14 38v10M24 40v12M40 40v12M50 38v10M12 20V8l8 3-8 3M52 20V8l-8 3 8 3"/></svg>
    <span>Sports &amp; Stadia</span></div>
  <div class="ind hexclip" style="left:608px;top:140px">
    <svg viewBox="0 0 64 64"><path d="M8 26h10l24-14v40L18 38H8zM18 38l4 16h8l-4-16M48 22a10 10 0 0 1 0 20"/><circle cx="30" cy="32" r="5"/></svg>
    <span>Brand Activations</span></div>
  <div class="ind hexclip" style="left:840px;top:140px">
    <svg viewBox="0 0 64 64"><rect x="20" y="4" width="24" height="8"/><path d="M8 22l4-10h40l4 10zM8 22c0 4 6 4 8 0 0 4 6 4 8 0 0 4 6 4 8 0 0 4 6 4 8 0 0 4 6 4 8 0 0 4 6 4 8 0M12 28v28h40V28M26 56V40h12v16M6 56h52"/></svg>
    <span>Retail &amp; Stores</span></div>
  <div class="ind hexclip" style="left:259px;top:345px">
    <svg viewBox="0 0 64 64"><path d="M10 8h44v10H10zM10 8l10 10M20 8l10 10M30 8l10 10M40 8l10 10M12 18v38M52 18v38M6 56h52M20 32v10h24V32M24 32l4 -6 4 6 4-6 4 6"/></svg>
    <span>Events &amp; Festivals</span></div>
  <div class="ind hexclip active" style="left:492px;top:345px">
    <svg viewBox="0 0 64 64"><path d="M10 32l6-16h32l6 16M6 32h52v14H6zM10 46v8h8v-8M46 46v8h8v-8M22 40h20"/><circle cx="14" cy="39" r="3"/><circle cx="50" cy="39" r="3"/></svg>
    <span>Automotive</span></div>
  <div class="ind hexclip" style="left:724px;top:345px">
    <svg viewBox="0 0 64 64"><path d="M6 22l26-12 26 12v20L32 54 6 42zM6 22l26 12 26-12M32 34v20"/><rect x="14" y="30" width="10" height="10"/><circle cx="44" cy="36" r="5"/></svg>
    <span>Exhibitions</span></div>
</section>

<section class="wave" role="img" aria-label="Glowing lime particle wave"></section>

<section class="about">
  <h2>ABOUT <em>US</em></h2>
  <div class="bar" style="left:143px;top:118px"></div>
  <div class="copy">
    <p>Lorem ipsum dolor sit amet, consectetur adipiscing elit, sed do eiusmod tempor incididunt ut labore et dolore magna aliqua. Ut enim ad minim veniam, quis nostrud exercitation ullamco laboris nisi ut aliquip ex ea commodo consequat.</p>
    <p>Duis aute irure dolor in reprehenderit in voluptate velit esse cillum dolore eu fugiat nulla pariatur. Excepteur sint occaecat cupidatat non proident, sunt in culpa qui officia deserunt mollit anim id est quia magni dolores laborum.</p>
  </div>
  <div class="btn-lime">Learn More</div>
  <div class="about-hex hexclip" role="img" aria-label="Collage of modular cabins and white event marquees on site"></div>
</section>

<section class="contact">
  <svg class="contact-bg" viewBox="0 0 1200 570" preserveAspectRatio="none">
    <polygon points="0,180 600,5 1200,180 1200,570 0,570" fill="#c6ff02"/>
    <polyline points="0,180 600,5 1200,180" fill="none" stroke="#fff" stroke-width="5"/>
  </svg>
  <h2>CONTACT US</h2>
  <h4 style="left:145px">Get In Touch</h4>
  <div class="field" style="left:143px;top:255px;width:240px"><svg viewBox="0 0 10 10"><circle cx="5" cy="3" r="2.2"/><path d="M1 10a4 4 0 0 1 8 0"/></svg>Name</div>
  <div class="field" style="left:397px;top:255px;width:239px"><svg viewBox="0 0 10 10"><path d="M2 1l2 2-1 1.5 2.5 2.5L7 6l2 2-1.5 1.5C4 9 1 6 .5 2.5z"/></svg>Phone Number</div>
  <div class="field" style="left:143px;top:310px;width:240px"><svg viewBox="0 0 10 10"><rect x="1" y="2" width="8" height="6"/><path d="M1 2l4 3 4-3"/></svg>Email Address</div>
  <div class="field" style="left:397px;top:310px;width:239px"><svg viewBox="0 0 10 10"><path d="M1 9l1-3 5-5 2 2-5 5z"/></svg>Subject</div>
  <div class="field" style="left:143px;top:365px;width:493px;height:85px"><svg viewBox="0 0 10 10"><path d="M1 1h8v6H4L1 9z"/></svg>Messagge</div>
  <div class="submit">SUBMIT</div>

  <h4 style="left:698px">Contact Details</h4>
  <div class="detail" style="top:252px"><svg viewBox="0 0 40 34"><path d="M20 2a10 10 0 0 1 10 10c0 8-10 20-10 20S10 20 10 12A10 10 0 0 1 20 2z"/><circle cx="20" cy="12" r="3.5"/></svg><div><b>ADDRESS</b><small>48 Harbor Lane, Westbrook, Kentshire KT4 2RD</small></div></div>
  <div class="detail" style="top:322px"><svg viewBox="0 0 40 34"><path d="M8 3h7l2 7-4 3a18 18 0 0 0 9 9l3-4 7 2v7c0 2-2 4-4 4C16 31 4 19 4 7c0-2 2-4 4-4z"/><path d="M24 4a10 10 0 0 1 9 9M24 9a5 5 0 0 1 4 4"/></svg><div><b>PHONE NUMBER</b><small>07700 900418</small></div></div>
  <div class="detail" style="top:388px"><svg viewBox="0 0 40 34"><rect x="4" y="6" width="32" height="22"/><path d="M4 6l16 13 16-13M4 28l12-11M36 28 24 17"/></svg><div><b>EMAIL</b><small>sales@ketrav.example</small></div></div>
</section>

<footer class="site-footer">
  <div class="brand"><span class="mark"></span>KETRAV</div>
  <div class="footnav"><span>HOME</span><i>/</i><span>THE SOLUTIONS</span><i>/</i><span>PLRANGE</span><i>/</i><span>THE INDUSTRIES</span><i>/</i><span>THE COMPANY</span><i>/</i><span>CONTACT US</span></div>
  <div class="copyright">Copyright© 2024 <u>Ketrav</u> | All Rights Reserved</div>
  <div class="footsocial"><span></span><span></span><span></span><span></span></div>
</footer>

</body>
</html>
```